Director of a child care centre business card

Corinne Helbrook - Director/ Owner
418 Fernlow Rd
Bayswater, 3153
Phone - 03 9581-4726
Fax - 03 95814727
info@tinybrambles.com.au
www.tinybrambles.com.au

Also needing another card same information but the name will be Yvette Colder - Centre Director

```html
<!DOCTYPE html>
<html lang="en">
<head>
<meta charset="utf-8">
<title>Tiny Brambles – Business Cards</title>
<link rel="stylesheet" href="https://fonts.googleapis.com/css2?family=Quicksand:wght@400;500;600&display=swap">
<style>
  :root {
    --backdrop: #0e1a3a;
    --card-blue: #1f2f86;
    --card-white: #ffffff;
    --accent-pink: #e43bd8;
    --accent-violet: #8a6be0;
    --accent-green: #7ed321;
    --text-light: #f2f2ff;
  }
  * { margin: 0; padding: 0; box-sizing: border-box; }
  html, body {
    width: 1200px; height: 900px; overflow: hidden;
    background: var(--backdrop);
    font-family: "Quicksand", sans-serif;
  }
  .canvas { position: relative; width: 1200px; height: 900px; }

  .card {
    position: absolute;
    width: 560px; height: 320px;
    overflow: hidden;
  }

  /* Front */
  .card--front {
    left: 70px; top: 90px;
    background: var(--card-blue);
    display: flex; flex-direction: column; align-items: center; justify-content: center;
  }
  .brand {
    display: flex; align-items: center; gap: 14px;
  }
  .brand__dot {
    width: 26px; height: 26px; border-radius: 50%;
    background: var(--accent-green);
  }
  .brand__name {
    font-weight: 500; font-size: 48px; color: var(--accent-pink);
    letter-spacing: 1px;
  }
  .tagline {
    margin-top: 6px;
    font-size: 17px; color: var(--text-light); letter-spacing: 1px;
  }

  /* Back */
  .card--back { left: 570px; top: 500px; background: var(--card-white); }
  .card__shape { position: absolute; inset: 0; }
  .person {
    position: absolute; left: 26px; top: 124px;
    width: 262px;
  }
  .person__name {
    font-size: 28px; font-weight: 500; color: var(--accent-pink);
    white-space: nowrap; line-height: 1.15;
  }
  .person__role {
    margin-top: 2px; margin-left: 56px;
    font-size: 12px; color: var(--accent-pink);
  }
  .brand--small {
    position: absolute; right: 28px; top: 58px; gap: 8px;
  }
  .brand--small .brand__dot { width: 14px; height: 14px; }
  .brand--small .brand__name { font-size: 20px; letter-spacing: 0; }

  .contacts {
    position: absolute; right: 22px; top: 170px;
    list-style: none; text-align: right;
  }
  .contacts li {
    display: flex; justify-content: flex-end; align-items: center; gap: 7px;
    font-size: 12.5px; line-height: 23px; color: var(--accent-pink);
  }
  .contacts svg { width: 13px; height: 13px; flex: none; }
</style>
</head>
<body>
<main class="canvas">

  <section class="card card--front" aria-label="Business card front">
    <div class="brand">
      <span class="brand__dot"></span>
      <span class="brand__name">Tiny Brambles</span>
    </div>
    <p class="tagline">Child Care And Kinder</p>
  </section>

  <section class="card card--back" aria-label="Business card back">
    <svg class="card__shape" viewBox="0 0 560 320" preserveAspectRatio="none">
      <path d="M345 0 C 300 90, 285 220, 310 320 L560 320 L560 0 Z" fill="var(--card-blue)"/>
      <path d="M348 -4 C 318 70, 300 170, 272 300" fill="none" stroke="var(--accent-pink)" stroke-width="2"/>
      <path d="M356 -4 C 326 80, 310 180, 286 304" fill="none" stroke="var(--accent-violet)" stroke-width="1.5"/>
      <path d="M364 -4 C 336 90, 320 190, 300 310" fill="none" stroke="var(--accent-violet)" stroke-width="1"/>
    </svg>

    <div class="person">
      <p class="person__name">Corinne Helbrook</p>
      <p class="person__role">Director/ Owner</p>
    </div>

    <div class="brand brand--small">
      <span class="brand__dot"></span>
      <span class="brand__name">Tiny Brambles</span>
    </div>

    <ul class="contacts">
      <li>03 9581-4726
        <svg viewBox="0 0 16 16"><path d="M4 1 L6 5 L4.5 6.5 C5.5 8.5 7.5 10.5 9.5 11.5 L11 10 L15 12 L13.5 15 C7 14 2 9 1 2.5 Z" fill="var(--accent-green)"/></svg></li>
      <li>03 95814727
        <svg viewBox="0 0 16 16"><rect x="2" y="5" width="12" height="8" rx="1" fill="var(--accent-green)"/><rect x="4" y="2" width="8" height="4" fill="var(--accent-green)"/></svg></li>
      <li>info@tinybrambles.com.au
        <svg viewBox="0 0 16 16"><rect x="1" y="3" width="14" height="10" rx="1" fill="var(--accent-green)"/><path d="M1 3 L8 9 L15 3" fill="none" stroke="var(--card-blue)" stroke-width="1.2"/></svg></li>
      <li>www.tinybrambles.com.au
        <svg viewBox="0 0 16 16"><circle cx="8" cy="8" r="7" fill="var(--accent-green)"/><path d="M1 8 H15 M8 1 C4 5 4 11 8 15 C12 11 12 5 8 1" fill="none" stroke="var(--card-blue)" stroke-width="1"/></svg></li>
      <li>418 Fernlow Rd Bayswater 3153
        <svg viewBox="0 0 16 16"><path d="M8 15 C4 10 3 8 3 6 A5 5 0 0 1 13 6 C13 8 12 10 8 15 Z" fill="var(--accent-green)"/><circle cx="8" cy="6" r="2" fill="var(--card-blue)"/></svg></li>
    </ul>
  </section>

</main>
</body>
</html>
```